Letterhead for Midwest Law Firm

Our law firm does estate planning and trust administration in Wisconsin and Illinois. We recently obtained a new logo and need to incorporate it into new stationary. The stationary needs to list out the attorneys at the firm, but we will want 3 variations, one with three attorneys, one with six, and one with six plus the names of states where each is licensed to practice (possibly as an asterisk with notation somewhere towards bottom of page. As with most traditional law practices, letterhead should be conservative and convey predictability and reliability. We view our brand as being primarily reliability, with prestige as a secondary element. We are upmarket, but would like to avoid seeming pretentious or "slick". We are a smaller firm with a personal touch.

Target Market(s)

Affluent Midwestern Americans approaching at or approaching retirement age.

Industry/Entity Type

Legal

Font styles to use
Serif
Sans Serif

Requirements
Must have
• Must use our logo. Must comply with Brennick Legal Guild Ethics rules: https://www.halvorjudic.org/courts/offices/docs/pqmtnv20annotated.pdf. Must be conventional. Must list names of attorneys and provide contact information for firm. Note that we are asking for three designs with very minor variations. Also, designer must provide letterhead in a format that is industry-standard for stationary printers.
Nice to have
• We would appreciate an alternate version that will look reasonable when printed on a black-and-white printer. Designer can use judgment as to whether to have use grayscale, black/white, or something in between.
Should not have
• No "motto" or "visit our website" extraneous materials. putting the website address somewhere is fine, but overall there is a lot of required text, and we'd like to not appear cluttered.

```html
<!DOCTYPE html>
<html lang="en">
<head>
<meta charset="utf-8">
<title>Halloway &amp; Brandt LLP — Letterhead, Colour and Grayscale</title>
<link rel="stylesheet" href="https://fonts.googleapis.com/css2?family=Libre+Baskerville&family=Noto+Sans:wght@400;500&display=swap">
<style>
  :root {
    --canvas: #ffffff;
    --sheet-edge: #b9b9b9;
    --ink: #1c1c1c;
    --navy: #1f2a44;
    --accent-blue: #0ea5dc;
    --accent-gold: #f2ae2e;
    --mono-black: #000000;
    --mono-gray: #6b6b6b;
    --band-text-colour: #1c1c1c;
    --band-text-mono: #ffffff;
  }
  * { box-sizing: border-box; margin: 0; padding: 0; }
  html, body {
    width: 1200px; height: 790px; overflow: hidden;
    background: var(--canvas);
  }
  body {
    position: relative;
    font-family: "Noto Sans", Arial, sans-serif;
    color: var(--ink);
  }
  .sheet {
    position: absolute; top: 24px;
    width: 558px; height: 721px;
    background: #fff;
    border: 1px solid var(--sheet-edge);
    box-shadow: 0 14px 22px -12px rgba(0,0,0,0.18);
    overflow: hidden;
  }
  .sheet--colour { left: 22px; --top-rule: var(--accent-blue); --accent: var(--accent-gold); --band-text: var(--band-text-colour); --firm: var(--navy); }
  .sheet--mono   { left: 612px; --top-rule: var(--mono-black); --accent: var(--mono-black); --band: var(--mono-gray); --band-text: var(--band-text-mono); --firm: var(--mono-black); }
  .sheet--colour { --band: var(--accent-gold); }

  .top-rule { position: absolute; left: 0; top: 0; width: 100%; height: 8px; background: var(--top-rule); }

  .firm-name {
    position: absolute; left: 20px; top: 58px;
    display: flex; align-items: center; gap: 8px;
    font-family: "Libre Baskerville", Georgia, serif;
    font-size: 13.5px; color: var(--firm); white-space: nowrap;
  }
  .firm-name .mark { width: 12px; height: 12px; border-radius: 50%; background: var(--firm); }

  .letter-date {
    position: absolute; right: 24px; top: 70px;
    font-size: 10px; padding: 0 10px 3px;
    border-bottom: 2px solid var(--accent);
  }
  .salutation, .closing, .enclosure { position: absolute; font-size: 10px; }
  .salutation { left: 20px; top: 174px; }
  .closing    { left: 18px; top: 540px; }
  .enclosure  { left: 20px; top: 595px; }

  .staff-band { position: absolute; left: 0; top: 654px; width: 558px; height: 20px; }
  .staff-band svg { position: absolute; inset: 0; }
  .staff-band polygon { fill: var(--band); }
  .staff-band .member {
    position: absolute; top: 0; height: 20px; line-height: 20px;
    font-size: 9.5px; color: var(--band-text); white-space: nowrap;
  }
  .member--one   { left: 12px; }
  .member--two   { left: 208px; }
  .member--three { right: 10px; }

  .contact {
    position: absolute; top: 684px; font-size: 10px; line-height: 13px;
  }
  .contact--phone   { left: 19px; }
  .contact--address { right: 24px; text-align: right; }
</style>
</head>
<body>

<section class="sheet sheet--colour" aria-label="Letterhead, colour version">
  <div class="top-rule"></div>
  <div class="firm-name"><span class="mark"></span>Halloway &amp; Brandt LLP</div>
  <p class="letter-date">March 17, 2021</p>
  <p class="salutation">Dear Sir/Madam,</p>
  <p class="closing">Sincerely,</p>
  <p class="enclosure">Enclosure</p>
  <div class="staff-band">
    <svg width="558" height="20" viewBox="0 0 558 20" aria-hidden="true">
      <polygon points="0,0 198,0 182,20 0,20"/>
      <polygon points="204,0 398,0 382,20 188,20"/>
      <polygon points="404,0 558,0 558,20 388,20"/>
    </svg>
    <span class="member member--one">WALTER J. HALLOWAY, Attorney</span>
    <span class="member member--two">THOMAS E. HALLOWAY, Attorney</span>
    <span class="member member--three">CAROL A. BENNING, Paralegal</span>
  </div>
  <p class="contact contact--phone">Telephone 414-555-0182<br>FAX 414-555-0164</p>
  <p class="contact contact--address">220 East Marlow Avenue, Suite 300<br>Milwaukee, Wisconsin 53210</p>
</section>

<section class="sheet sheet--mono" aria-label="Letterhead, grayscale version">
  <div class="top-rule"></div>
  <div class="firm-name"><span class="mark"></span>Halloway &amp; Brandt LLP</div>
  <p class="letter-date">March 17, 2021</p>
  <p class="salutation">Dear Sir/Madam,</p>
  <p class="closing">Sincerely,</p>
  <p class="enclosure">Enclosure</p>
  <div class="staff-band">
    <svg width="558" height="20" viewBox="0 0 558 20" aria-hidden="true">
      <polygon points="0,0 198,0 182,20 0,20"/>
      <polygon points="204,0 398,0 382,20 188,20"/>
      <polygon points="404,0 558,0 558,20 388,20"/>
    </svg>
    <span class="member member--one">WALTER J. HALLOWAY, Attorney</span>
    <span class="member member--two">THOMAS E. HALLOWAY, Attorney</span>
    <span class="member member--three">CAROL A. BENNING, Paralegal</span>
  </div>
  <p class="contact contact--phone">Telephone 414-555-0182<br>FAX 414-555-0164</p>
  <p class="contact contact--address">220 East Marlow Avenue, Suite 300<br>Milwaukee, Wisconsin 53210</p>
</section>

</body>
</html>
```